BOOK COVER FOR LEADING INTERNATIONAL KEYNOTE SPEAKER

We need a book cover that is bold, adventurous and powerful.
About the book: To go after your triggers and the things you are afraid of and breakthroughs (in life and business) are on the other side of it. Inside is a 5 step proven process to actually do so. The book itself is experiential so if that idea can be incorporated in the cover that would be awesome.
This isn't your typical self help book and the cover should reflect that. Stay away from cheesy and think outside of the box.
Book title: Chasing Unease
Subtext: How to get breakthrough results in life and business, no matter what
Author: Marlowe Pendry
Cover concept: Emphasize "Breakthrough"
Idea to play with: torn paper revealing "Unease"
Designer to choose colors to be used in the design.

```html
<!DOCTYPE html>
<html lang="en">
<head>
<meta charset="utf-8">
<title>Chasing Unease — Marlowe Pendry</title>
<link rel="stylesheet" href="https://fonts.googleapis.com/css2?family=Anton&family=Comfortaa:wght@500&display=swap">
<style>
  :root {
    --charcoal: #2b2d30;
    --chartreuse: #c9cc48;
    --white: #ffffff;
  }
  html, body {
    margin: 0;
    padding: 0;
    overflow: hidden;
    background: var(--charcoal);
  }
  .cover {
    position: relative;
    width: 680px;
    height: 1200px;
    overflow: hidden;
    background: var(--charcoal);
  }
  .chevrons {
    position: absolute;
    inset: 0;
    width: 680px;
    height: 1200px;
  }
  .chevrons polygon { fill: var(--chartreuse); }
  .title {
    position: absolute;
    left: 0;
    right: 0;
    top: 70px;
    margin: 0;
    text-align: center;
    color: var(--white);
    font-family: "Anton", "Impact", sans-serif;
    font-weight: 400;
    font-size: 172px;
    line-height: 176px;
    letter-spacing: 1px;
  }
  .title span { display: block; }
  .subtitle {
    position: absolute;
    left: 110px;
    right: 80px;
    top: 424px;
    margin: 0;
    color: var(--white);
    font-family: "Comfortaa", sans-serif;
    font-weight: 500;
    font-size: 24px;
    line-height: 31px;
  }
  .author {
    position: absolute;
    left: 0;
    right: 0;
    top: 1130px;
    margin: 0;
    text-align: center;
    color: var(--white);
    font-family: "Comfortaa", sans-serif;
    font-weight: 500;
    font-size: 26px;
  }
</style>
</head>
<body>
  <main class="cover">
    <svg class="chevrons" viewBox="0 0 680 1200" aria-hidden="true">
      <polygon points="0,-107 219,-308 680,116 680,347 219,-77 0,124"/>
      <polygon points="0,355 219,154 680,578 680,809 219,385 0,586"/>
      <polygon points="0,817 219,616 680,1040 680,1271 219,847 0,1048"/>
      <polygon points="0,1279 219,1078 680,1502 680,1733 219,1309 0,1510"/>
    </svg>
    <h1 class="title"><span>Chasing</span><span>Unease</span></h1>
    <p class="subtitle">How to get breakthrough results in life and business, no matter what!</p>
    <p class="author">Marlowe Pendry</p>
  </main>
</body>
</html>
```